IT Services Postcard

I am looking to update and refresh my existing postcard. I would like to keep all the content it has , but make it more modern and elegant. We are a small boutique IT firm here in Miami, FL in business for 15 years. We support all Veltrosa products. I would like highlight that as well on the postcard- "15 years serving South Florida". I would also like to make the following revisions to the bullet points:Change "Included Email & Virus Protection" to Included Antivirus SoftwareChange "Quarnex Plus Remote Control" to "Secure remote computer access"Add the following bullet point "Included Deskora 520 Backup"You can certainly change the images for the bullet points, and refresh the colors and background as well. I have uploaded a copy of the front and back of my last flyer. I target small to medium size businesses who need a good local IT company they can trust. I look forward to working with you. Thank you.
Target Market(s)
Small Businesses
Industry/Entity Type
It Professional
Colors
Designer to choose colors to be used in the design.
Look and feel

```html
<!DOCTYPE html>
<html lang="en">
<head>
<meta charset="utf-8">
<title>Kestrova Tech Postcard</title>
<link href="https://fonts.googleapis.com/css2?family=Open+Sans:wght@400;600;700;800&display=swap" rel="stylesheet">
<style>
:root{
  --page:#ececec;
  --sky-top:#c9e6f2;
  --sky-bottom:#f4f8fb;
  --band:#6b83c0;
  --orange:#ea6a1c;
  --ink:#1f1f1f;
  --charcoal:#262626;
  --white:#ffffff;
  --icon-fill:#dfe9f7;
  --badge:#3f64ad;
  --badge-light:#dfe3ec;
  --lavender:#d6dcf0;
  --arrow:#3f5fb0;
}
*{box-sizing:border-box;margin:0;padding:0}
html,body{width:1200px;height:1200px;overflow:hidden;background:var(--page);font-family:"Open Sans",Arial,sans-serif}
.canvas{position:relative;width:1200px;height:1200px}
.card{position:absolute;left:208px;width:757px;height:534px;overflow:hidden;background:var(--white)}
.card--front{top:64px}
.card--back{top:640px;background:linear-gradient(160deg,#f6f7fc 0%,var(--lavender) 100%)}
.abs{position:absolute}

.brand{left:34px;top:44px;color:var(--ink)}
.brand__name{font-size:44px;font-weight:800;letter-spacing:1px;line-height:1}
.brand__tag{font-size:17px;font-weight:700;letter-spacing:.5px;margin-left:124px;margin-top:4px}

.sky{left:0;top:0;width:757px;height:140px;background:linear-gradient(180deg,var(--sky-top),var(--sky-bottom))}
.monitor-art{left:560px;top:8px;width:152px;height:176px;border-radius:10px;background:linear-gradient(160deg,#f4f6fa,#b9c3d3)}
.services{left:0;top:140px;width:757px;height:234px;background:var(--band)}
.services__title{left:37px;top:12px;color:var(--white);font-size:23px;font-weight:700}
.svc{position:absolute;display:flex;align-items:center;gap:12px;color:var(--white);font-size:13px}
.svc__icon{width:32px;height:32px;border-radius:50%;background:var(--icon-fill);border:3px solid var(--white);flex:none}

.years{left:602px;top:292px}
.other{left:31px;top:380px}
.other__title{color:var(--orange);font-size:23px;font-weight:700}
.other__list{margin-top:4px;font-size:12.5px;font-weight:600;color:var(--ink);white-space:nowrap}
.other__list span{color:var(--arrow)}

.cta{left:0;top:436px;width:580px;height:60px;background:var(--charcoal);clip-path:polygon(0 0,100% 0,93% 100%,0 100%)}
.cta__small{position:absolute;left:32px;top:8px;color:var(--orange);font-size:16px;font-weight:700}
.cta__big{position:absolute;left:32px;top:25px;color:var(--orange);font-size:24px;font-weight:700;letter-spacing:.2px;white-space:nowrap}
.badges{display:flex;gap:12px;align-items:center}
.badge{height:30px;border-radius:3px}
.badge--a{width:52px;background:var(--badge-light)}
.badge--b{width:54px;background:var(--badge)}
.badge--c{width:40px;background:var(--badge-light)}

.contact{display:flex;align-items:center;gap:10px;font-size:13px;color:var(--ink);white-space:nowrap}
.contact svg{flex:none}
.contact--front{left:39px;top:500px;gap:8px}
.contact--front .gap{width:14px}

.stamp{left:623px;top:30px;width:82px;height:75px;background:#efefef}
.slogan{left:444px;top:448px;width:313px;height:42px;background:var(--orange);clip-path:polygon(8% 0,100% 0,100% 100%,0 100%);color:var(--white);font-size:22px;font-weight:700;display:flex;align-items:center;justify-content:flex-end;padding-right:36px}
.footer{left:0;top:490px;width:757px;height:44px;background:var(--band);justify-content:center;color:var(--white);font-size:16px}
</style>
</head>
<body>
<div class="canvas">

  <section class="card card--front">
    <div class="abs sky"></div>
    <div class="abs brand">
      <div class="brand__name">KESTROVA TECH</div>
      <div class="brand__tag">MANAGED SERVICES</div>
    </div>
    <div class="abs monitor-art" role="img" aria-label="Illustration of a desktop monitor showing business charts"></div>

    <div class="abs services">
      <h2 class="abs services__title">Our Low cost monthly IT Service includes:</h2>
      <div class="svc" style="left:50px;top:40px"><span class="svc__icon"></span>24/7 Monitoring of Service</div>
      <div class="svc" style="left:50px;top:78px"><span class="svc__icon"></span>Proactive Desktop &amp; Server Maintenance</div>
      <div class="svc" style="left:50px;top:115px"><span class="svc__icon"></span>Unlimited Onsite &amp; Remote Support</div>
      <div class="svc" style="left:50px;top:153px"><span class="svc__icon"></span>Antivirus Software Change</div>
      <div class="svc" style="left:50px;top:190px"><span class="svc__icon"></span>Monthly Network Health Report</div>
      <div class="svc" style="left:421px;top:41px"><span class="svc__icon"></span>Secure remote computer access</div>
      <div class="svc" style="left:421px;top:79px"><span class="svc__icon"></span>Veltrosa Certified Technicians</div>
      <div class="svc" style="left:421px;top:116px"><span class="svc__icon"></span>Fast Response Times</div>
      <div class="svc" style="left:421px;top:154px"><span class="svc__icon"></span>No Long Term Contracts</div>
      <div class="svc" style="left:421px;top:191px"><span class="svc__icon"></span>Deskora 520 Backup</div>
    </div>

    <svg class="abs years" width="140" height="140" viewBox="0 0 140 140">
      <circle cx="70" cy="66" r="66" fill="#fff"/>
      <circle cx="70" cy="56" r="47" fill="#4f6db8"/>
      <circle cx="70" cy="56" r="44" fill="var(--orange)"/>
      <text x="70" y="64" text-anchor="middle" font-family="Open Sans, sans-serif" font-weight="800" font-size="38" fill="#fff">15</text>
      <text x="70" y="86" text-anchor="middle" font-family="Open Sans, sans-serif" font-weight="700" font-size="17" fill="#fff">YEARS</text>
      <path id="arcYears" d="M9,56 A61,61 0 0,0 131,56" fill="none"/>
      <text font-family="Open Sans, sans-serif" font-weight="700" font-size="12" fill="#1f1f1f">
        <textPath href="#arcYears" startOffset="50%" text-anchor="middle">Serving South Florida</textPath>
      </text>
    </svg>

    <div class="abs other">
      <div class="other__title">Other Services Offered:</div>
      <div class="other__list"><span>➤</span>Onsite/Offside Backup Solution <span>➤</span>Deskora 520 Migration <span>➤</span>Harbrook Business Voice Edge Installation</div>
    </div>

    <div class="abs cta">
      <div class="cta__small">CALL TODAY AND</div>
      <div class="cta__big">GET 2 FREE HOURS OF ONSITE SERVICE</div>
    </div>
    <div class="abs badges" style="left:568px;top:454px">
      <span class="badge badge--a"></span><span class="badge badge--b"></span><span class="badge badge--c"></span>
    </div>

    <div class="abs contact contact--front">
      <span>Contact us Today</span><span class="gap"></span>
      <svg width="16" height="16" viewBox="0 0 16 16"><circle cx="8" cy="8" r="7" fill="none" stroke="#ea6a1c" stroke-width="1.3"/><ellipse cx="8" cy="8" rx="3" ry="7" fill="none" stroke="#ea6a1c" stroke-width="1.1"/><path d="M1 8h14M2.5 4.5h11M2.5 11.5h11" stroke="#ea6a1c" stroke-width="1"/></svg>
      <span>www.kestrovatech.com</span><span class="gap"></span>
      <svg width="16" height="16" viewBox="0 0 16 16"><path d="M3 1l3 3-1.5 2a9 9 0 005 5l2-1.5 3 3-2 2C7 15 1 9 1 3z" fill="#ea6a1c"/></svg>
      <span>305.555.0142</span><span class="gap"></span>
      <svg width="16" height="12" viewBox="0 0 16 12"><rect x="1" y="1" width="14" height="10" fill="none" stroke="#ea6a1c" stroke-width="1.2"/><path d="M1 1l7 6 7-6M1 11l5-4M15 11l-5-4" fill="none" stroke="#ea6a1c" stroke-width="1.1"/></svg>
      <span>support@kestrovatech.com</span>
    </div>
  </section>

  <section class="card card--back">
    <div class="abs brand">
      <div class="brand__name">KESTROVA TECH</div>
      <div class="brand__tag">MANAGED SERVICES</div>
    </div>
    <div class="abs stamp"></div>
    <div class="abs badges" style="left:38px;top:430px">
      <span class="badge badge--a" style="height:34px;width:66px"></span><span class="badge badge--b" style="height:34px;width:70px"></span><span class="badge badge--c" style="height:34px;width:52px"></span>
    </div>
    <div class="abs slogan">Relax, we can fix IT!</div>
    <div class="abs contact footer">
      <span>Contact us Today</span>
      <svg width="17" height="17" viewBox="0 0 16 16"><circle cx="8" cy="8" r="7" fill="none" stroke="#fff" stroke-width="1.3"/><ellipse cx="8" cy="8" rx="3" ry="7" fill="none" stroke="#fff" stroke-width="1.1"/><path d="M1 8h14M2.5 4.5h11M2.5 11.5h11" stroke="#fff" stroke-width="1"/></svg>
      <span>www.kestrovatech.com</span>
      <svg width="17" height="17" viewBox="0 0 16 16"><path d="M3 1l3 3-1.5 2a9 9 0 005 5l2-1.5 3 3-2 2C7 15 1 9 1 3z" fill="#fff"/></svg>
      <span>305.555.0142</span>
      <svg width="16" height="12" viewBox="0 0 16 12"><rect x="1" y="1" width="14" height="10" fill="none" stroke="#fff" stroke-width="1.2"/><path d="M1 1l7 6 7-6" fill="none" stroke="#fff" stroke-width="1.1"/></svg>
      <span>support@kestrovatech.com</span>
    </div>
  </section>

</div>
</body>
</html>
```